Travel Blogger Business Card for roamquill.net

I need a two-sided business card for a travel blogging website. The card should be both professional and fun at the same time. This is for the website www.roamquill.net

I don't necessarily think that the current logo on the website needs to be used on the business card but it can be. I am very flexible with ideas

Target Market(s)

Travel agencies that will be met at a conference.

Industry/Entity Type

Travel

Contact Information for Business Card

Company Name: Roam Quill.net
Name: Bertrand Olesky
Voice: +1-(345)-402-7731
Address: Coral Reach Shore, Grand Cayman, Cayman Islands
Email: ceo@roamquill.net

Colors
0592cd
0355a3
3176b5
33a6d7
85cae6
85acd3

Requirements
Must have
• Website address and name should be bigger than address, phone number, and email.

```html
<!DOCTYPE html>
<html lang="en">
<head>
<meta charset="utf-8">
<title>Roam Quill business card</title>
<link href="https://fonts.googleapis.com/css2?family=Encode+Sans+Semi+Condensed:wght@300;400;600;800&display=swap" rel="stylesheet">
<style>
  :root {
    --bg: #e9edf1;
    --white: #ffffff;
    --brand-blue: #2391d0;
    --navy: #1f3a60;
    --tab-navy: #1e3a63;
    --icon-1: #3176b5;
    --icon-2: #33a6d7;
    --icon-3: #85cae6;
    --icon-4: #85acd3;
    --text-light: #ffffff;
  }
  * { box-sizing: border-box; margin: 0; padding: 0; }
  html, body { width: 1200px; height: 891px; overflow: hidden; }
  body {
    background: var(--bg);
    font-family: "Encode Sans Semi Condensed", Arial, sans-serif;
    position: relative;
  }
  .card {
    position: absolute;
    width: 540px;
    height: 309px;
    background: var(--white);
    overflow: hidden;
    box-shadow: 0 6px 18px rgba(20, 40, 70, 0.18);
  }
  .card--front { left: 40px; top: 291px; }
  .card--back { left: 620px; top: 291px; }

  .wordmark {
    display: flex;
    align-items: center;
    gap: 10px;
    color: var(--brand-blue);
    font-weight: 800;
    text-transform: uppercase;
    letter-spacing: 0.5px;
    white-space: nowrap;
  }
  .wordmark__dot {
    width: 16px; height: 16px;
    border-radius: 50%;
    background: var(--brand-blue);
    flex: none;
  }

  /* Front */
  .card--front .wordmark {
    position: absolute;
    left: 0; right: 0; top: 108px;
    justify-content: center;
    font-size: 34px;
  }
  .front-band {
    position: absolute;
    left: 0; right: 0; bottom: 0;
    height: 117px;
    background: var(--brand-blue);
  }
  .front-tab {
    position: absolute;
    left: 180px; top: 192px;
    width: 220px; height: 40px;
  }
  .front-tab svg { position: absolute; inset: 0; }
  .front-tab__url {
    position: absolute; inset: 0;
    display: flex; align-items: center; justify-content: center;
    color: var(--text-light);
    font-size: 13px;
    letter-spacing: 0.3px;
  }

  /* Back */
  .back-accent {
    position: absolute;
    left: 0; top: 0;
    width: 8px; height: 150px;
    background: var(--brand-blue);
  }
  .card--back .wordmark {
    position: absolute;
    left: 0; width: 228px; top: 98px;
    justify-content: center;
    gap: 8px;
    font-size: 22px;
  }
  .card--back .wordmark__dot { width: 11px; height: 11px; }
  .back-panel {
    position: absolute;
    left: 228px; top: 0; right: 0; bottom: 0;
    background: var(--navy);
  }
  .icon-column {
    position: absolute;
    left: 228px; top: 46px;
    display: flex; flex-direction: column;
  }
  .icon-tile {
    width: 34px; height: 34px;
    display: flex; align-items: center; justify-content: center;
  }
  .icon-tile--person { background: var(--icon-1); }
  .icon-tile--phone { background: var(--icon-2); }
  .icon-tile--pin { background: var(--icon-3); }
  .icon-tile--globe { background: var(--icon-4); }
  .contact {
    position: absolute;
    left: 276px; top: 44px;
    color: var(--text-light);
  }
  .contact__name {
    font-size: 27px;
    font-weight: 300;
    line-height: 36px;
  }
  .contact__phone {
    font-size: 16px;
    font-weight: 300;
    line-height: 24px;
    margin-top: 4px;
  }
  .contact__email {
    font-size: 13px;
    font-weight: 300;
    line-height: 18px;
  }
  .contact__address {
    font-size: 13px;
    font-weight: 300;
    line-height: 17px;
    margin-top: 4px;
  }
  .contact__web {
    font-size: 20px;
    font-weight: 300;
    margin-top: 12px;
  }
</style>
</head>
<body>

  <section class="card card--front" aria-label="Card front">
    <div class="wordmark">
      <span class="wordmark__dot"></span>
      <span class="wordmark__name">Roam Quill</span>
    </div>
    <div class="front-band"></div>
    <div class="front-tab">
      <svg width="220" height="40" viewBox="0 0 220 40" aria-hidden="true">
        <polygon points="0,0 220,0 200,40 20,40" fill="var(--tab-navy)"/>
      </svg>
      <span class="front-tab__url">www.roamquill.net</span>
    </div>
  </section>

  <section class="card card--back" aria-label="Card back">
    <div class="back-accent"></div>
    <div class="wordmark">
      <span class="wordmark__dot"></span>
      <span class="wordmark__name">Roam Quill</span>
    </div>
    <div class="back-panel"></div>

    <div class="icon-column">
      <div class="icon-tile icon-tile--person">
        <svg width="16" height="16" viewBox="0 0 16 16" aria-hidden="true">
          <circle cx="8" cy="5" r="3.2" fill="#fff"/>
          <path d="M2 15c0-3.6 2.7-5.6 6-5.6s6 2 6 5.6z" fill="#fff"/>
        </svg>
      </div>
      <div class="icon-tile icon-tile--phone">
        <svg width="16" height="16" viewBox="0 0 16 16" aria-hidden="true">
          <path d="M4 1.5l2.3 3-1.4 1.6c.8 1.9 2.2 3.3 4 4.1l1.6-1.4 3 2.3-1.3 2.6C7 13.5 2.5 9 1.4 3z" fill="#fff"/>
        </svg>
      </div>
      <div class="icon-tile icon-tile--pin">
        <svg width="16" height="16" viewBox="0 0 16 16" aria-hidden="true">
          <path d="M8 1a5 5 0 0 0-5 5c0 3.6 5 9 5 9s5-5.4 5-9a5 5 0 0 0-5-5z" fill="#fff"/>
          <circle cx="8" cy="6" r="1.8" fill="var(--icon-3)"/>
        </svg>
      </div>
      <div class="icon-tile icon-tile--globe">
        <svg width="16" height="16" viewBox="0 0 16 16" aria-hidden="true">
          <circle cx="8" cy="8" r="6.3" fill="none" stroke="#fff" stroke-width="1.4"/>
          <ellipse cx="8" cy="8" rx="2.7" ry="6.3" fill="none" stroke="#fff" stroke-width="1.2"/>
          <line x1="1.7" y1="8" x2="14.3" y2="8" stroke="#fff" stroke-width="1.2"/>
        </svg>
      </div>
    </div>

    <div class="contact">
      <p class="contact__name">Bertrand Olesky</p>
      <p class="contact__phone">+1-(345)-402-7731</p>
      <p class="contact__email">ceo@roamquill.net</p>
      <p class="contact__address">Coral Reach Shore, Grand Cayman,<br>Cayman Islands</p>
      <p class="contact__web">www.roamquill.net</p>
    </div>
  </section>

</body>
</html>
```